Financial Service Company Need Business Card Design

This is a new startup company, first of its kind to offer this service. We facilitate the movement of deposit funds electronically between home buyers and real estate brokerages.Our customers are DOMIVANS®, real estate brokerages, and home buyers, we identify ourselves as a financial/technology company.
Not looking for anything too flashy. Just a clean design that shows the logo, contact info, etc. Company colors can be seen on attached logo, and 'coming soon page'
www.quorvanta.ca

```html
<!DOCTYPE html>
<html lang="en">
<head>
<meta charset="utf-8">
<title>Quorvanta Business Card</title>
<link href="https://fonts.googleapis.com/css2?family=Open+Sans:wght@400;600;700&display=swap" rel="stylesheet">
<style>
  :root {
    --backdrop: #d2d3d5;
    --paper: #ffffff;
    --brand-orange: #f15a29;
    --ink-grey: #646464;
    --on-orange: #ffffff;
  }
  * { margin: 0; padding: 0; box-sizing: border-box; }
  html, body {
    width: 1200px;
    height: 900px;
    overflow: hidden;
    background: var(--backdrop);
    font-family: "Open Sans", Arial, sans-serif;
  }
  .canvas {
    position: relative;
    width: 1200px;
    height: 900px;
  }
  .card {
    position: absolute;
    left: 298px;
    width: 604px;
    height: 336px;
  }
  .card--front { top: 79px; background: var(--paper); }
  .card--back { top: 484px; background: var(--brand-orange); }

  .wordmark {
    position: absolute;
    display: flex;
    align-items: center;
    gap: 12px;
    font-weight: 600;
    letter-spacing: -0.5px;
    line-height: 1;
  }
  .wordmark__square {
    display: block;
    background: currentColor;
  }
  .card--front .wordmark {
    left: 47px;
    top: 48px;
    font-size: 36px;
    color: var(--ink-grey);
  }
  .card--front .wordmark__square {
    width: 30px;
    height: 30px;
    background: var(--brand-orange);
  }
  .card--back .wordmark {
    left: 50%;
    top: 148px;
    transform: translateX(-50%);
    font-size: 46px;
    color: var(--on-orange);
  }
  .card--back .wordmark__square { width: 40px; height: 40px; }

  .holder {
    position: absolute;
    left: 47px;
    top: 182px;
  }
  .holder__name {
    color: var(--brand-orange);
    font-weight: 700;
    font-size: 20px;
    line-height: 24px;
  }
  .holder__title {
    color: var(--ink-grey);
    font-size: 18px;
    letter-spacing: 1px;
    line-height: 26px;
  }

  .contact {
    position: absolute;
    left: 366px;
    top: 176px;
    list-style: none;
    color: var(--ink-grey);
    font-size: 16px;
    letter-spacing: 1px;
    line-height: 26.8px;
  }

  .website {
    position: absolute;
    left: 0;
    width: 564px;
    top: 300px;
    text-align: center;
    color: var(--on-orange);
    font-size: 18px;
    letter-spacing: 5px;
  }
</style>
</head>
<body>
<main class="canvas">
  <section class="card card--front">
    <div class="wordmark"><span class="wordmark__square"></span>Quorvanta</div>
    <div class="holder">
      <p class="holder__name">xxxx xxxxx</p>
      <p class="holder__title">Director</p>
    </div>
    <ul class="contact">
      <li>xxxx xxxx xxxx</li>
      <li>xxxx xxxx</li>
      <li>P:(555) 555-5555</li>
      <li>F:(555) 555-5555</li>
      <li>yourmail@mailbox.com</li>
    </ul>
  </section>

  <section class="card card--back">
    <div class="wordmark"><span class="wordmark__square"></span>Quorvanta</div>
    <p class="website">www.xxxxxxxx.com</p>
  </section>
</main>
</body>
</html>
```